4' x 8' Construction Project Sign, think of a very large business card

We need project signs for our construction sites, the sign will be mounted along the road so cars driving by can quickly read. the sign should be able to be read as cars drive by doing highway speed.

Think like your making a large business card

I would like to include "NOW HIRING" Superintendents, Project Managers, Pipe Foremen, Pipe Layers, and Equipment Operators

Description of services we provide should include

Civil Construction Services
Land Clearing
Excavation
Underground Utilities
Environmental Maintenance

The 2 objectives is to market to future clients and to recruit new employees

The sign will be mounted on posts at the entrance of our construction projects

Low design quality

Target Market(s)

Construction and land developers

Industry/Entity Type

Construction Company

Font styles to use
Other font styles liked:
• Hypatia Sans Pro lite

Colors

Designer to choose colors to be used in the design.

Requirements
Must have
• Clean and easy to read
• Civil Construction Services
• Land Clearing
• Excavation
• Underground Utilities
• Road Construction

```html
<!DOCTYPE html>
<html lang="en">
<head>
<meta charset="utf-8">
<title>Harlow Brothers Civil Construction – Project Sign</title>
<link href="https://fonts.googleapis.com/css2?family=Alegreya+Sans:wght@500;700&display=swap" rel="stylesheet">
<style>
  :root {
    --brand-blue: #213f7e;
    --navy-line: #1e3a78;
    --charcoal: #3a3a3c;
    --ink: #111214;
    --hire-red: #e5141b;
    --white: #ffffff;
    --link-blue: #8fb6f2;
    --page: #ffffff;
  }
  html, body {
    margin: 0;
    width: 1200px;
    height: 1200px;
    overflow: hidden;
    background: var(--page);
    font-family: "Alegreya Sans", Arial, sans-serif;
  }
  .sign {
    position: absolute;
    left: 0;
    top: 300px;
    width: 1610px;
    height: 804px;
    transform: scale(0.74534);
    transform-origin: 0 0;
    overflow: hidden;
    background: linear-gradient(180deg, #d3d3d3 0%, #f2f2f2 45%, #ffffff 70%);
  }
  .sign-shapes { position: absolute; inset: 0; }
  .brand-square {
    position: absolute;
    left: 383px; top: 60px;
    width: 180px; height: 180px;
    background: var(--brand-blue);
  }
  .brand-divider {
    position: absolute;
    left: 617px; top: 25px;
    width: 3px; height: 253px;
    background: #6b6b6e;
  }
  .brand-name {
    position: absolute;
    left: 655px; top: 52px;
    color: var(--brand-blue);
    font-weight: 500;
    line-height: 1;
  }
  .brand-name .line-main { display: block; font-size: 102px; letter-spacing: 2px; }
  .brand-name .line-sub { display: block; font-size: 58px; letter-spacing: 25px; margin-top: 10px; }
  .section-title {
    position: absolute;
    margin: 0;
    font-weight: 700;
    line-height: 1;
  }
  .services-title { left: 382px; top: 306px; font-size: 54px; color: var(--brand-blue); }
  .hiring-title { left: 418px; top: 500px; font-size: 56px; color: var(--hire-red); }
  .bullet-row {
    position: absolute;
    display: flex;
    gap: 22px;
    margin: 0; padding: 0;
    list-style: none;
    font-size: 36px;
    font-weight: 700;
    color: var(--ink);
    line-height: 1;
  }
  .bullet-row li { display: flex; align-items: center; }
  .bullet-row li::before {
    content: "";
    width: 15px; height: 13px;
    margin-right: 16px;
    background: var(--brand-blue);
  }
  .row-1 { left: 390px; top: 364px; }
  .row-2 { left: 394px; top: 405px; }
  .row-3 { left: 398px; top: 446px; }
  .row-4 { left: 428px; top: 557px; }
  .row-5 { left: 428px; top: 598px; }
  .contact-phone {
    position: absolute;
    left: 405px; top: 690px;
    display: flex; align-items: center; gap: 22px;
    color: var(--white);
    font-size: 104px; font-weight: 700; line-height: 1;
  }
  .contact-links {
    position: absolute;
    left: 1160px; top: 696px;
    margin: 0; padding: 0; list-style: none;
    color: var(--link-blue);
    font-size: 40px; font-weight: 500; line-height: 1;
  }
  .contact-links li { display: flex; align-items: center; gap: 16px; height: 47px; }
</style>
</head>
<body>
  <div class="sign">
    <svg class="sign-shapes" viewBox="0 0 1610 804" width="1610" height="804" aria-hidden="true">
      <polygon points="0,0 228,0 365,804 0,804" fill="#213f7e"/>
      <polygon points="246,0 394,655 394,804 378,804" fill="#3a3a3c"/>
      <rect x="390" y="655" width="1217" height="21" fill="#1e3a78"/>
      <polygon points="392,682 1610,682 1610,804 378,804" fill="#3a3a3c"/>
    </svg>

    <div class="brand-square"></div>
    <div class="brand-divider"></div>
    <div class="brand-name">
      <span class="line-main">HARLOW BROTHERS</span>
      <span class="line-sub">CIVIL CONSTRUCTION</span>
    </div>

    <h2 class="section-title services-title">SERVICES WE PROVIDE</h2>
    <ul class="bullet-row row-1"><li>ROAD CONSTRUCTION</li><li>SANITARY SEWER CONSTRUCTION</li></ul>
    <ul class="bullet-row row-2"><li>SITE PREPARATION &amp; EXCAVATION</li><li>STORMWATER DRAINAGE</li></ul>
    <ul class="bullet-row row-3"><li>WATERMAIN CONSTRUCTION</li><li>SHORELINE RESTORATION</li></ul>

    <h2 class="section-title hiring-title">NOW HIRING</h2>
    <ul class="bullet-row row-4"><li>SUPERINTENDENTS</li><li>PROJECT MANAGERS</li><li>PIPE FOREMEN</li></ul>
    <ul class="bullet-row row-5"><li>PIPE LAYERS</li><li>EQUIPMENT OPERATORS</li></ul>

    <div class="contact-phone">
      <svg width="66" height="66" viewBox="0 0 24 24" aria-hidden="true">
        <path fill="#ffffff" d="M6.6 10.8a15.1 15.1 0 0 0 6.6 6.6l2.2-2.2c.3-.3.7-.4 1-.2 1.1.4 2.3.6 3.6.6.6 0 1 .4 1 1V20c0 .6-.4 1-1 1A17 17 0 0 1 3 4c0-.6.4-1 1-1h3.5c.6 0 1 .4 1 1 0 1.3.2 2.5.6 3.6.1.3 0 .7-.2 1z"/>
        <path fill="none" stroke="#ffffff" stroke-width="1.3" d="M14 2.5a7.5 7.5 0 0 1 7.5 7.5M14 5.5a4.5 4.5 0 0 1 4.5 4.5"/>
      </svg>
      <span>555-014-2200</span>
    </div>

    <ul class="contact-links">
      <li>
        <svg width="26" height="22" viewBox="0 0 26 22" aria-hidden="true"><rect x="1" y="5" width="24" height="16" fill="none" stroke="#8fb6f2" stroke-width="2"/><path d="M1 5l12 9 12-9" fill="none" stroke="#8fb6f2" stroke-width="2"/></svg>
        <span>Info@HarlowCivil.com</span>
      </li>
      <li>
        <svg width="26" height="26" viewBox="0 0 26 26" aria-hidden="true"><circle cx="13" cy="13" r="11" fill="none" stroke="#8fb6f2" stroke-width="2"/><ellipse cx="13" cy="13" rx="5" ry="11" fill="none" stroke="#8fb6f2" stroke-width="2"/><path d="M2 13h22M4 7h18M4 19h18" stroke="#8fb6f2" stroke-width="1.5"/></svg>
        <span>&nbsp;www.HarlowCivil.com</span>
      </li>
    </ul>
  </div>
</body>
</html>
```